"Bel Amora" Wholesale Box Design

We are a wholesale fruit distributing company and we have to create our own cherry packaging design.
These cherries are from Canada, and will be exported to several countries. They must accentuate the premium quality we are packing!
This box must work well for our customers all over the world (North America, Asia, Middle East, Europe, etc).
We prefer a cartoon-ish style, similar to our other labels.
Go crazy, make it as wild or as conservative as you want. Let's see what you can come up with!

Target Market(s)

Fruit importers and supermarkets.
Asian, Middle Eastern, European customers.

Industry/Entity Type

Wholesale

Colors

Designer to choose colors to be used in the design.

Requirements
Must have
• Style similar to our other labels (examples attached).
• It must include the following, as seen in the attached sample box:
• - PRODUCT OF CANADA
• - PRODUIT DU CANADA
• - CATEGORY No. 1
• - 5kg - 11lb
• It must include our logo (see attached), and show the following text:
• - Distributed by: Quilby Traders, Dunmore Falls, NV 89071 USA
• - www.quilbytraders.example
• It must be maximum 3 colors (and/or a combination of them).
Nice to have
• Would like to see a feminine looking cherry. "Bel Amora" means "My Dear" in French, but also sounds like a "My Cherry".

```html
<!DOCTYPE html>
<html lang="en">
<head>
<meta charset="utf-8">
<title>Quilby Traders – Bel Amora Box</title>
<link href="https://fonts.googleapis.com/css2?family=Abril+Fatface&family=Montserrat:wght@400;600;700&family=Raleway:wght@300&display=swap" rel="stylesheet">
<style>
  :root {
    --backdrop: #a9a9a9;
    --board: #ffffff;
    --cut-line: #8f8f8f;
    --cherry-red: #a6192e;
    --leaf-green: #78a22f;
    --ink: #1c1c1c;
    --title: #f4f4f4;
  }
  * { margin: 0; padding: 0; box-sizing: border-box; }
  html, body { width: 1200px; height: 1198px; overflow: hidden; background: var(--backdrop); }
  .canvas { position: relative; width: 1200px; height: 1198px; background: var(--backdrop); font-family: "Montserrat", sans-serif; }
  .sheet-title {
    position: absolute; left: 97px; top: 56px;
    font-family: "Raleway", sans-serif; font-weight: 300; font-size: 27px; letter-spacing: 0.5px; color: var(--title);
  }
  .panel { position: absolute; background: var(--board); border: 1px solid var(--cut-line); overflow: hidden; }
  .flap { top: 188px; height: 154px; }
  .flap-bottom { top: 890px; height: 156px; }
  .flap-end-left { left: 99px; width: 170px; }
  .flap-end-right { left: 931px; width: 169px; }
  .flap-main { left: 268px; width: 664px; overflow: visible; border-left: none; border-right: none; }

  .side { top: 356px; height: 522px; width: 156px; }
  .side-left { left: 99px; }
  .side-right { left: 944px; }

  .base { position: absolute; left: 256px; top: 342px; width: 688px; height: 548px; background: var(--board); border: 14px solid var(--leaf-green); }

  .handle { position: absolute; background: var(--board); border: 1px solid var(--cut-line); border-radius: 10px; }

  .cherry-art {
    position: absolute; border-radius: 50%;
    background: radial-gradient(circle at 38% 35%, #c42a3e 0%, var(--cherry-red) 55%, #8e1426 100%);
  }

  .brand-mark { position: absolute; display: flex; align-items: center; gap: 6px; }
  .brand-mark .dot { width: 30px; height: 30px; border-radius: 50%; background: var(--leaf-green); flex: none; }
  .brand-mark .name { font-family: "Montserrat", sans-serif; font-weight: 600; color: var(--leaf-green); line-height: 0.95; }

  .product-name {
    position: absolute; font-family: "Abril Fatface", serif; color: var(--ink); line-height: 0.88; white-space: nowrap;
  }
  .heart { position: absolute; }

  .category-label { position: absolute; font-size: 12px; color: var(--ink); letter-spacing: 0.2px; }
  .category-value { position: absolute; font-size: 28px; color: var(--ink); font-weight: 400; }

  .face-content { position: absolute; inset: 0; }
  .flap-bottom .face-content { transform: rotate(180deg); }

  .strip { position: absolute; width: 522px; height: 156px; left: calc(50% - 261px); top: calc(50% - 78px); }
  .side-left .strip { transform: rotate(-90deg); }
  .side-right .strip { transform: rotate(90deg); }

  .origin-info { position: absolute; font-size: 8px; line-height: 1.25; color: var(--ink); }
  .origin-info .origin { font-weight: 700; color: var(--cherry-red); font-size: 9.5px; }
  .weight { position: absolute; font-family: "Abril Fatface", serif; color: var(--leaf-green); font-size: 18px; white-space: nowrap; }
  .label-window { position: absolute; border: 1px solid var(--cut-line); border-radius: 4px; background: var(--board); }
</style>
</head>
<body>
<div class="canvas">
  <h1 class="sheet-title">QUILBY TRADERS - BEL AMORA BOX - 3 PANTONE COLORS</h1>

  <!-- Top flap -->
  <div class="panel flap flap-end-left"></div>
  <div class="panel flap flap-end-right"></div>
  <div class="panel flap flap-main">
    <div class="face-content">
      <div class="brand-mark" style="left:28px;top:22px;">
        <span class="dot"></span><span class="name" style="font-size:20px;">quilby<br>traders</span>
      </div>
      <span class="category-label" style="left:75px;top:92px;">CATEGORY</span>
      <svg class="heart" style="left:42px;top:109px;" width="30" height="26" viewBox="0 0 30 26" aria-hidden="true"><path d="M15 26 C6 19 0 14 0 7.5 C0 3 3.5 0 7.5 0 C11 0 13.5 2 15 5 C16.5 2 19 0 22.5 0 C26.5 0 30 3 30 7.5 C30 14 24 19 15 26Z" fill="var(--cherry-red)"/></svg>
      <span class="category-value" style="left:76px;top:104px;">No.1</span>
      <div class="cherry-art" role="img" aria-label="Winking cherry character with stem and leaf" style="left:172px;top:38px;width:66px;height:66px;"></div>
      <div class="product-name" style="left:244px;top:12px;font-size:56px;">Bel<br>amora</div>
      <div class="cherry-art" role="img" aria-label="Smiling cherry character waving" style="left:480px;top:40px;width:110px;height:102px;"></div>
    </div>
  </div>

  <!-- Side panels -->
  <div class="panel side side-left">
    <div class="strip">
      <div class="brand-mark" style="left:18px;top:10px;">
        <span class="dot" style="width:22px;height:22px;"></span><span class="name" style="font-size:15px;">quilby<br>traders</span>
      </div>
      <div class="origin-info" style="left:10px;top:76px;">
        <div class="origin">PRODUCT OF CANADA<br>PRODUIT DU CANADA</div>
        CATEGORY No. 1<br>Distributed by: Quilby Traders,<br>Dunmore Falls, NV 89071 USA<br>www.quilbytraders.example
      </div>
      <div class="label-window" style="left:178px;top:50px;width:168px;height:80px;"></div>
      <div class="product-name" style="left:358px;top:48px;font-size:28px;">Bel<br>amora</div>
      <div class="weight" style="left:358px;top:118px;">5kg - 11lb</div>
      <div class="cherry-art" role="img" aria-label="Small cherry character hugging itself" style="left:442px;top:14px;width:62px;height:70px;"></div>
    </div>
  </div>

  <div class="panel side side-right">
    <div class="strip">
      <div class="brand-mark" style="left:18px;top:12px;">
        <span class="dot" style="width:22px;height:22px;"></span><span class="name" style="font-size:15px;">quilby<br>traders</span>
      </div>
      <div class="origin-info" style="left:18px;top:66px;">
        <div class="origin">PRODUCT OF CANADA<br>PRODUIT DU CANADA</div>
        CATEGORY No. 1<br>Distributed by: Quilby Traders,<br>Dunmore Falls, NV 89071 USA<br>www.quilbytraders.example
      </div>
      <div class="cherry-art" role="img" aria-label="Cherry character waving with stem and leaf" style="left:210px;top:14px;width:104px;height:100px;"></div>
      <div class="product-name" style="left:352px;top:48px;font-size:28px;">Bel<br>amora</div>
      <div class="weight" style="left:352px;top:18px;">5kg - 11lb</div>
      <div class="cherry-art" role="img" aria-label="Small winking cherry character" style="left:444px;top:22px;width:54px;height:54px;"></div>
    </div>
  </div>

  <!-- Base -->
  <div class="base">
    <div class="cherry-art" role="img" aria-label="Winking cherry character with stem and leaf" style="left:240px;top:100px;width:152px;height:150px;"></div>
    <div class="cherry-art" role="img" aria-label="Dancing cherry character with arms, legs, stem and leaf" style="left:384px;top:196px;width:212px;height:184px;"></div>
    <div class="brand-mark" style="left:40px;top:170px;">
      <span class="dot" style="width:56px;height:56px;"></span><span class="name" style="font-size:31px;">quilby<br>traders</span>
    </div>
    <svg class="heart" style="left:32px;top:280px;" width="68" height="60" viewBox="0 0 30 26" aria-hidden="true"><path d="M15 26 C6 19 0 14 0 7.5 C0 3 3.5 0 7.5 0 C11 0 13.5 2 15 5 C16.5 2 19 0 22.5 0 C26.5 0 30 3 30 7.5 C30 14 24 19 15 26Z" fill="var(--cherry-red)"/></svg>
    <div class="product-name" style="left:102px;top:258px;font-size:82px;">Bel<br>amora</div>
  </div>

  <!-- Base side handles -->
  <div class="handle" style="left:262px;top:431px;width:36px;height:62px;"></div>
  <div class="handle" style="left:262px;top:741px;width:36px;height:62px;"></div>
  <div class="handle" style="left:902px;top:431px;width:36px;height:62px;"></div>
  <div class="handle" style="left:902px;top:741px;width:36px;height:62px;"></div>

  <!-- Bottom flap -->
  <div class="panel flap-bottom flap-end-left"></div>
  <div class="panel flap-bottom flap-end-right"></div>
  <div class="panel flap-bottom flap-main">
    <div class="face-content">
      <div class="brand-mark" style="left:28px;top:22px;">
        <span class="dot"></span><span class="name" style="font-size:20px;">quilby<br>traders</span>
      </div>
      <span class="category-label" style="left:75px;top:92px;">CATEGORY</span>
      <svg class="heart" style="left:42px;top:109px;" width="30" height="26" viewBox="0 0 30 26" aria-hidden="true"><path d="M15 26 C6 19 0 14 0 7.5 C0 3 3.5 0 7.5 0 C11 0 13.5 2 15 5 C16.5 2 19 0 22.5 0 C26.5 0 30 3 30 7.5 C30 14 24 19 15 26Z" fill="var(--cherry-red)"/></svg>
      <span class="category-value" style="left:76px;top:104px;">No.1</span>
      <div class="cherry-art" role="img" aria-label="Winking cherry character with stem and leaf" style="left:172px;top:38px;width:66px;height:66px;"></div>
      <div class="product-name" style="left:244px;top:12px;font-size:56px;">Bel<br>amora</div>
      <div class="cherry-art" role="img" aria-label="Smiling cherry character waving" style="left:480px;top:40px;width:110px;height:102px;"></div>
    </div>
  </div>

  <!-- Flap handles -->
  <div class="handle" style="left:446px;top:305px;width:125px;height:44px;"></div>
  <div class="handle" style="left:627px;top:305px;width:125px;height:44px;"></div>
  <div class="handle" style="left:446px;top:884px;width:125px;height:42px;"></div>
  <div class="handle" style="left:627px;top:884px;width:125px;height:42px;"></div>
</div>
</body>
</html>
```